Looking for potential sellers

We help people buy and sell homes and are currently looking for potential home sellers. We offer low commissions, are the Local Colorado Springs and Falcon Experts, homes selling fast and at top dollar, Free expert pricing opinions and Consultations, over 9 years of experience, top rated Realtors creative and aggressive marketing strategies. Never merely own a house, THRIVE at Harborview. phone number 482-630-9157 web thriveatharborview.com

```html
<!DOCTYPE html>
<html lang="en">
<head>
<meta charset="UTF-8">
<title>Find the Home of Your Dreams – Harborview Real Estate Company</title>
<link href="https://fonts.googleapis.com/css2?family=Montserrat:wght@500;600;700&display=swap" rel="stylesheet">
<style>
  :root {
    --navy: #1a2736;
    --navy-deep: #141f2c;
    --olive: #8d9c2c;
    --olive-bright: #9aab33;
    --white: #ffffff;
    --headline-dark: rgba(26, 39, 54, 0.88);
    --sky-top: #3f6fae;
    --sky-low: #9cb6d3;
    --brick: #a4573a;
    --siding: #d9cdb2;
  }
  * { box-sizing: border-box; margin: 0; padding: 0; }
  html, body {
    width: 1200px;
    height: 798px;
    overflow: hidden;
    background: var(--white);
    font-family: "Montserrat", Arial, sans-serif;
  }
  .flyer {
    position: relative;
    width: 1200px;
    height: 798px;
    overflow: hidden;
    background: var(--navy);
  }
  .hero-photo {
    position: absolute;
    left: 0; top: 0;
    width: 1200px;
    height: 578px;
    background: linear-gradient(180deg, var(--sky-top) 0%, var(--sky-low) 30%, var(--brick) 42%, #8f4c34 70%, var(--siding) 88%, #6b6a62 100%);
  }
  .headline {
    position: absolute;
    left: 66px;
    top: 224px;
    color: var(--white);
    font-weight: 600;
    text-transform: uppercase;
    line-height: 1;
  }
  .headline-line {
    display: block;
    width: max-content;
    padding: 0 22px;
    font-size: 47px;
    letter-spacing: 0.5px;
  }
  .headline-line--accent {
    background: var(--olive);
    height: 83px;
    line-height: 83px;
  }
  .headline-line--dark {
    margin-top: 5px;
    background: var(--headline-dark);
    height: 71px;
    line-height: 71px;
  }
  .brand {
    position: absolute;
    left: 0;
    top: 578px;
    width: 392px;
    height: 220px;
    display: flex;
    align-items: center;
    justify-content: center;
    gap: 12px;
    white-space: nowrap;
  }
  .brand-mark {
    flex: none;
    width: 20px;
    height: 20px;
    border-radius: 50%;
    background: var(--olive-bright);
  }
  .brand-name {
    color: var(--white);
    font-weight: 600;
    font-size: 25px;
    letter-spacing: 0.3px;
  }
  .pitch {
    position: absolute;
    left: 420px;
    top: 614px;
    width: 764px;
    color: var(--white);
    font-weight: 600;
    font-size: 18.5px;
    line-height: 1.33;
    text-align: center;
  }
  .contact-bar {
    position: absolute;
    left: 392px;
    top: 732px;
    width: 808px;
    height: 66px;
    padding: 0 24px;
    background: var(--olive);
    display: flex;
    align-items: center;
    justify-content: center;
    color: var(--navy-deep);
    font-weight: 700;
    font-size: 24px;
    white-space: nowrap;
  }
  .contact-bar .sep { margin: 0 10px; }
</style>
</head>
<body>
  <main class="flyer">
    <div class="hero-photo" role="img" aria-label="Photo of a row of modern two-storey townhomes with red and cream siding, stone bases and white porch railings under a blue sky"></div>

    <h1 class="headline">
      <span class="headline-line headline-line--accent">Find the home of</span>
      <span class="headline-line headline-line--dark">your dreams</span>
    </h1>

    <div class="brand">
      <span class="brand-mark"></span>
      <span class="brand-name">Harborview Real Estate</span>
    </div>

    <p class="pitch">There’s never been a better time to sell your home in Colorado Springs! With home values rising almost 10% in the last year alone, and predicted to jump another 3.7% within the year, it truly is a seller’s market!.</p>

    <div class="contact-bar">
      <span>CALL US : 482-630-9157</span>
      <span class="sep">•</span>
      <span>info@thriveatharborview.com</span>
    </div>
  </main>
</body>
</html>
```